Business Card Design

I am a video director/cameraman and photographer. I cover documentaries, corporate, government departments, educational and non profits. They could be on Tv, Vidflo or DVD to 10 or 10 thousand ppl. Some have been seen worldwide and won international awards.
I regard myself as bold and saturated...as in I want strong ideas of substance to come through in a film and that the info is valid, interesting and saturates the mind without it being geeky boring.
Need a great logo and layout for cards. My name is Barnaby Tolliver and my company is RT Media Productions.

Must have company name, my name, email, website, phone and type of films I do. I'll supply additional info for the back- which will be companies I have filmed for.

Attach image shows I like the boxes/icons idea but am open to yr ideas...Roar on!
Updates

Reason: I am charged by your designs. This is the first time I have used ths type of service and getting to know you guys is very good value for me. Please keep your creative spirit in this. I want a contemporary logo. Some have shown the way forward and a few need to show a clean, current looking image of my attitude by way of log and design. Thx to you all Barn

Industry/Entity Type

Government

```html
<!DOCTYPE html>
<html lang="en">
<head>
<meta charset="utf-8">
<title>RT Media Productions – Business Card</title>
<link href="https://fonts.googleapis.com/css2?family=Jost:wght@400;500&display=swap" rel="stylesheet">
<style>
  :root {
    --bg: #e9e6e1;
    --card: #0b0b0b;
    --card-sheen: #2a2a2a;
    --red: #e31b1b;
    --white: #ffffff;
    --grey: #d8d8d8;
  }
  * { box-sizing: border-box; margin: 0; padding: 0; }
  html, body {
    width: 1200px; height: 900px; overflow: hidden;
    background: var(--bg);
    font-family: "Jost", "Futura", sans-serif;
  }
  .canvas { position: relative; width: 1200px; height: 900px; }

  .card {
    position: absolute; left: 250px; width: 700px; height: 400px;
    border-radius: 18px; overflow: hidden;
    background: var(--card);
    color: var(--white);
    box-shadow: 0 10px 30px rgba(0,0,0,.25);
  }
  .card--front {
    top: 35px;
    background: linear-gradient(115deg, var(--card) 35%, var(--card-sheen) 60%, var(--card) 85%);
  }
  .card--back { top: 465px; }

  /* brand lockup */
  .brand { position: absolute; display: flex; align-items: center; }
  .brand__square { background: var(--red); flex: none; }
  .brand__name { font-weight: 400; color: var(--white); text-transform: uppercase; }
  .brand__name span { display: block; }

  .card--front .brand { left: 105px; top: 125px; gap: 18px; }
  .card--front .brand__square { width: 190px; height: 84px; }
  .card--front .brand__name { font-size: 40px; line-height: 40px; letter-spacing: 1px; }
  .tagline {
    position: absolute; left: 105px; top: 232px;
    font-size: 17.5px; font-weight: 500; letter-spacing: 1.6px; text-transform: uppercase;
  }

  /* back card */
  .gallery { position: absolute; left: 0; top: 0; width: 700px; height: 150px; display: flex; }
  .gallery__tile { flex: 1; height: 100%; }
  .tile--ice { background: linear-gradient(160deg, #c9d6e6, #eef3f8 45%, #b22530 70%, #dfe6ef); }
  .tile--tree { background: linear-gradient(170deg, #d9702a, #c2381e 45%, #5d5a2a 80%, #e9e4d7); }
  .tile--flower { background: radial-gradient(circle at 45% 50%, #c22a1f, #9a4418 45%, #b86a1b 80%); }
  .tile--lake { background: linear-gradient(180deg, #3f6fd8 0%, #b9c8e0 30%, #5a6b7e 50%, #1a8bc4 70%, #0d5f93); }
  .tile--bird { background: radial-gradient(circle at 55% 45%, #5fa8c8, #7aa43a 45%, #4e7d25 80%); }

  .rule { position: absolute; left: 0; top: 150px; width: 700px; height: 4px; background: var(--red); }

  .services {
    position: absolute; left: 0; top: 162px; width: 700px;
    display: flex; justify-content: center; align-items: center; gap: 14px;
    font-size: 14px; font-weight: 500; letter-spacing: .6px; color: var(--white);
    list-style: none;
  }
  .services li { display: flex; align-items: center; gap: 14px; }
  .services li + li::before {
    content: ""; width: 6px; height: 6px; background: var(--red); display: inline-block;
  }

  .divider { position: absolute; left: 0; top: 0; }

  .person { position: absolute; left: 40px; top: 222px; }
  .person__name { font-size: 27px; font-weight: 500; letter-spacing: 1px; text-transform: uppercase; }
  .person__name em { font-style: normal; color: var(--red); }
  .person__role { font-size: 14px; letter-spacing: .6px; color: var(--grey); margin-top: 2px; }

  .card--back .brand { left: 40px; top: 308px; gap: 12px; }
  .card--back .brand__square { width: 118px; height: 52px; }
  .card--back .brand__name { font-size: 24px; line-height: 25px; letter-spacing: 1px; }

  .contact { position: absolute; left: 420px; top: 220px; list-style: none; }
  .contact li { display: flex; align-items: center; gap: 12px; font-size: 18px; letter-spacing: .6px; line-height: 26px; }
  .contact svg { width: 13px; height: 13px; flex: none; }
</style>
</head>
<body>
<main class="canvas">

  <section class="card card--front" aria-label="Business card front">
    <div class="brand">
      <div class="brand__square"></div>
      <div class="brand__name"><span>RT Media</span><span>Productions</span></div>
    </div>
    <p class="tagline">Supporting your production to maximum exposure</p>
  </section>

  <section class="card card--back" aria-label="Business card back">
    <div class="gallery">
      <div class="gallery__tile tile--ice" role="img" aria-label="Photo of icicles with red berries"></div>
      <div class="gallery__tile tile--tree" role="img" aria-label="Photo of an autumn tree with red leaves"></div>
      <div class="gallery__tile tile--flower" role="img" aria-label="Photo of red blossoms close up"></div>
      <div class="gallery__tile tile--lake" role="img" aria-label="Photo of a mountain lake"></div>
      <div class="gallery__tile tile--bird" role="img" aria-label="Photo of a colourful bird on a branch"></div>
    </div>
    <div class="rule"></div>

    <ul class="services">
      <li>Documentaries</li>
      <li>Corporate</li>
      <li>TVC</li>
      <li>Government</li>
      <li>Educational</li>
      <li>Non Profits</li>
    </ul>

    <svg class="divider" width="700" height="400" viewBox="0 0 700 400" aria-hidden="true">
      <defs>
        <linearGradient id="divider-fade" x1="0" y1="0" x2="0" y2="1">
          <stop offset="0" stop-color="#e31b1b"/>
          <stop offset="1" stop-color="#e31b1b" stop-opacity="0"/>
        </linearGradient>
      </defs>
      <line x1="385" y1="195" x2="400" y2="300" stroke="url(#divider-fade)" stroke-width="1.5"/>
    </svg>

    <div class="person">
      <h1 class="person__name">Barnaby <em>Tolliver</em></h1>
      <p class="person__role">Video Director/Cameraman|Photographer</p>
    </div>

    <div class="brand">
      <div class="brand__square"></div>
      <div class="brand__name"><span>RT Media</span><span>Productions</span></div>
    </div>

    <ul class="contact">
      <li>
        <svg viewBox="0 0 16 16" aria-hidden="true"><path fill="#e31b1b" d="M3.6 1.5l2.3 2.6-1.2 1.8a9 9 0 005.4 5.4l1.8-1.2 2.6 2.3-1.4 2.1C7.4 14 2 8.6 1.5 2.9z"/></svg>
        +1234567980
      </li>
      <li>
        <svg viewBox="0 0 16 16" aria-hidden="true"><rect x="1" y="3" width="14" height="10" fill="#e31b1b"/><path d="M1 3l7 6 7-6" fill="none" stroke="#0b0b0b" stroke-width="1.4"/></svg>
        yourname@mailbox.com
      </li>
      <li>
        <svg viewBox="0 0 16 16" aria-hidden="true"><circle cx="9.5" cy="6.5" r="4.2" fill="none" stroke="#e31b1b" stroke-width="2"/><path d="M6.5 9.5L1.5 14.5" stroke="#e31b1b" stroke-width="2.4"/></svg>
        www.websitename.com
      </li>
    </ul>
  </section>

</main>
</body>
</html>
```